We need a binder cover. I have attached a photo of what we want it ot look like but use our logo, graphic and colour scheme. The dimensions are”
11.5Hx10.5W – front cover
11.5Hx1.5W – side spine
The Website is www.brightwayadvisory.ca
For keywords please use Dignity, Independence and Accessibility
As well, we are looking for 2 versions of letterhead .
1. Standard document layout to make table of contents,cover page (no address).
2. Standard letter head with address on the bottom of the page.
Our address is
418 Maple Crest Blvd East Unit 3 Suite 921
Oakville Ontario
K7R 4P3
Also want a CD labels for us,
1. With our logo and “Meridale Framework for Tenant Onboarding – Staff Training Session” Power Point with Audio
2. With our logo and “Meridale Framework for Tenant Onboarding – Staff Training Session” CD audio only format
3. With our logo and “ Copy of documentation for PWRB”

```html
<!DOCTYPE html>
<html lang="en">
<head>
<meta charset="utf-8">
<title>Brightway Advisory Inc. – Letterhead</title>
<link rel="stylesheet" href="https://fonts.googleapis.com/css2?family=Source+Sans+3:wght@600&family=PT+Serif&display=swap">
<style>
  :root {
    --brand-red: #e31e26;
    --charcoal: #3b3b3d;
    --paper: #ffffff;
  }
  html, body {
    margin: 0;
    padding: 0;
    width: 849px;
    height: 1200px;
    overflow: hidden;
    background: var(--paper);
  }
  .letterhead {
    position: relative;
    width: 849px;
    height: 1200px;
    background: var(--paper);
    overflow: hidden;
  }
  .letterhead__frame {
    position: absolute;
    inset: 0;
    display: block;
  }
  .frame-red { fill: var(--brand-red); }
  .frame-dark { fill: var(--charcoal); }
  .frame-gap { fill: var(--paper); }

  .brand {
    position: absolute;
    left: 146px;
    top: 132px;
    display: flex;
    align-items: center;
    gap: 14px;
  }
  .brand__mark {
    width: 40px;
    height: 40px;
    background: var(--brand-red);
  }
  .brand__name {
    margin: 0;
    font-family: "Source Sans 3", Arial, sans-serif;
    font-weight: 600;
    color: var(--charcoal);
    line-height: 1;
    letter-spacing: 0.5px;
  }
  .brand__name-main {
    display: block;
    font-size: 34px;
  }
  .brand__name-sub {
    display: block;
    font-size: 19px;
    margin-top: 3px;
  }

  .footer-web {
    position: absolute;
    left: 142px;
    right: 0;
    top: 1150px;
    margin: 0;
    text-align: center;
    font-family: "PT Serif", Georgia, serif;
    font-size: 15px;
    color: var(--brand-red);
    letter-spacing: 0.3px;
    transform: translateX(-140px);
  }
</style>
</head>
<body>
  <main class="letterhead">
    <svg class="letterhead__frame" width="849" height="1200" viewBox="0 0 849 1200" aria-hidden="true">
      <!-- top band -->
      <path class="frame-dark" d="M130 0 H849 V80 H210 Q150 80 135 30 Z"/>
      <!-- left red disc -->
      <circle class="frame-red" cx="-85" cy="155" r="240"/>
      <!-- white separation under disc -->
      <path class="frame-gap" d="M0 395 Q60 390 95 345 L95 420 L0 420 Z"/>
      <!-- left red strip -->
      <path class="frame-red" d="M0 400 Q18 398 28 390 V1200 H0 Z"/>
      <!-- bottom band -->
      <path class="frame-dark" d="M142 1200 V1150 Q142 1075 222 1075 H849 V1200 Z"/>
    </svg>

    <header class="brand">
      <span class="brand__mark"></span>
      <h1 class="brand__name">
        <span class="brand__name-main">BRIGHTWAY</span>
        <span class="brand__name-sub">ADVISORY INC.</span>
      </h1>
    </header>

    <p class="footer-web">www.brightwayadvisory.ca</p>
  </main>
</body>
</html>
```